Flyer
Zielgruppe
Ich bin Energieberater für Wohngebäude. Ich möchte ein Flyer über meine Leistungen erstellen. Dabei möchte ich gezielt potentielle Partner wie Architekten und Immobilienverwalter ansprechen und ein Netzwerk aufbauen.
Meine Leistungen im Überblick:
- Energieberatung
- Individueller Sanierungsfahrplan (iSFP)
- Energieausweise
- TbH-Effizienzhaus-Planung (Neubau und Bestand)
- Planung klimafreundlicher Neubau (KFN)
- Fördermittelberatung und -beantragung
- PUL-Einzelmaßnahmen wie z. B. Dämmung der Gebäudehülle oder Fenstertausch uvm.
- Heizlastberechnung nach DIN EN 12831
- Hydraulischer Abgleich nach Verfahren A/B
- Heizflächenauslegung
- Wärmepumpen (Beratung und Auslegung)
Meine Signatur:
M. Eng. Torben Wiskow
Energieberater / Planungsingenieur
Volmar Haus
Lindholzgasse 7C
47263 Gelsenkirchen
Tel: 0152 / 871 43 06
E-Mail: info@Volmar-Haus.de
Aufgabenstellung
Ich möchte den Flyer sowohl als PDF-Format nutzen, um Kalt-Akquise übers Internet zu betreiben, als auch ausgedruckt.

```html
<!DOCTYPE html>
<html lang="de">
<head>
<meta charset="utf-8">
<title>Volmar Haus – Flyer</title>
<link href="https://fonts.googleapis.com/css2?family=Exo+2:wght@400;500&family=Quicksand:wght@400;500;700&display=swap" rel="stylesheet">
<style>
:root{
  --bg:#d6d6d6;
  --paper:#f4f4f4;
  --blue:#1a5fb4;
  --blue-mid:#1c7cc4;
  --teal:#15a9b3;
  --ink:#2b2b2b;
  --muted:#555;
  --photo-top:#8f8f98;
  --photo-warm:#b9a594;
  --photo-dark:#5e5550;
}
*{box-sizing:border-box;margin:0;padding:0}
html,body{width:1200px;height:1200px;overflow:hidden}
body{background:var(--bg);font-family:"Quicksand",sans-serif;color:var(--ink);position:relative}
.panel{position:absolute;top:290px;width:280px;height:620px;background:var(--paper);overflow:hidden}
.cover{left:25px;box-shadow:0 8px 20px rgba(0,0,0,.18)}
.spread{position:absolute;left:335px;top:290px;width:840px;height:620px;box-shadow:0 8px 20px rgba(0,0,0,.18)}
.spread .panel{top:0}
.p1{left:0}.p2{left:280px}.p3{left:560px}
.p2,.p3{border-left:1px solid #e3e3e3}

.cover-photo{position:absolute;left:0;top:0;width:280px;height:370px;
  background:linear-gradient(180deg,var(--photo-top) 0%,#a9a4a6 35%,var(--photo-warm) 60%,var(--photo-dark) 100%);opacity:.85}
.cover-brand{position:absolute;top:140px;left:0;width:280px;text-align:center;color:#fff}
.cover-brand .dot{display:block;width:54px;height:54px;border-radius:50%;background:var(--blue-mid);margin:0 auto 12px}
.cover-brand .name{font-family:"Quicksand",sans-serif;font-weight:500;font-size:15px;letter-spacing:1px}
.band{position:absolute;left:0;width:100%;height:34px;background:linear-gradient(90deg,var(--blue),var(--teal))}
.cover .band{top:365px}
.cover-title{position:absolute;top:430px;width:100%;text-align:center;font-family:"Exo 2",sans-serif;color:var(--blue-mid);font-size:28px}
.cover-sub{position:absolute;top:476px;width:100%;text-align:center;font-size:13px;line-height:1.35;color:var(--ink)}
.cover-url{position:absolute;top:540px;left:30px;width:220px;height:34px;border:1.5px solid var(--blue-mid);border-radius:17px;text-align:center;line-height:31px;font-size:12px}

.heading{font-family:"Exo 2",sans-serif;font-weight:400;color:var(--blue-mid);font-size:24px;text-transform:uppercase;padding-bottom:8px;border-bottom:2px solid var(--teal);display:inline-block}
.p1 .heading{margin:34px 0 0 28px}
.about{margin:26px 24px 0 28px;font-size:10.5px;line-height:1.45}
.about p{margin-bottom:8px}
.p1 .band{top:250px;height:22px}
.about-photo{position:absolute;top:272px;left:0;width:280px;height:348px;
  background:linear-gradient(160deg,#e9e9e9,#d7d7d7 45%,#e8d6b8 70%,#cbd7e0)}

.person-card{position:absolute;left:18px;top:24px;width:244px;height:580px;border-radius:10px;
  background:linear-gradient(180deg,var(--teal) 0%,var(--blue-mid) 35%,var(--blue) 100%);color:#fff}
.portrait{position:absolute;left:14px;top:28px;width:82px;height:82px;border-radius:50%;border:4px solid #fff;background:linear-gradient(180deg,#8a6c5a,#3a302c)}
.person-title{position:absolute;left:116px;top:36px;font-family:"Exo 2",sans-serif;font-size:22px;line-height:1.15;text-align:center}
.person-text{position:absolute;left:18px;top:140px;width:210px;font-size:10px;line-height:1.5;text-align:justify}
.signature{position:absolute;left:18px;bottom:26px;font-size:10px;line-height:1.45}

.p3 .heading{margin:44px 0 0 28px}
.services{position:absolute;top:110px;left:14px;width:252px;display:grid;grid-template-columns:1fr 1fr;row-gap:14px;column-gap:6px}
.service{text-align:center;font-size:7px;line-height:1.3;color:var(--muted)}
.service svg{display:block;margin:0 auto 4px}
.service.last{grid-column:1 / span 2}
</style>
</head>
<body>

<section class="panel cover">
  <div class="cover-photo" role="img" aria-label="Foto eines modernen, abendlich beleuchteten Hauses"></div>
  <div class="cover-brand"><span class="dot"></span><span class="name">Volmar Haus</span></div>
  <div class="band"></div>
  <h1 class="cover-title">Volmar Haus</h1>
  <p class="cover-sub">Ingenieurtechnische Planung<br>in der Energiewende!</p>
  <div class="cover-url">www.volmar-haus.de</div>
</section>

<div class="spread">
  <section class="panel p1">
    <h2 class="heading">Über uns</h2>
    <div class="about">
      <p>Wir sind Ihr Partner, wenn es um planerische Belange in Ihrem Haus geht.</p>
      <p>Unser Anspruch an uns selbst ist es, hoch qualitative und verlässliche Arbeit zu leisten, um Ihren Ansprüchen mehr als zu genügen!</p>
      <p>Wir sind nur deshalb so erfolgreich, weil wir unsere Arbeit mit Leib und Seele leisten!</p>
    </div>
    <div class="band"></div>
    <div class="about-photo" role="img" aria-label="Foto mit Thermostat, Energieeffizienzskala, Hausmodell, Taschenrechner und Münzen auf Bauplänen"></div>
  </section>

  <section class="panel p2">
    <div class="person-card">
      <div class="portrait" role="img" aria-label="Porträtfoto von Torben Wiskow"></div>
      <h2 class="person-title">Zu<br>Meiner<br>Person</h2>
      <p class="person-text">Mein Name ist <strong>Torben Wiskow</strong> und ich bin ein freiberuflicher Ingenieur, der seinen Know-How als Ingenieur in der Energiewende einsetzt. Aufnahme der aktuellen Heizungstechnik, Berechnung ihrer Heizlast und Heizflächen sowie das Abgleichen der Hydraulik ist mein Kerngebiet. Basierend auf dieser Ergebnisse prüfe ich, ob ihr Gebäude mit der aktuellen Anlagentechnik, Dämmwerten und den Heizflächen Wärmepumpentauglich ist. Falls dies nicht der Fall sein sollte, erstelle ich einen Sanierungsfahrplan, wie wir Ihr Haus gemeinsam Wärmepumpentauglich machen können. Dabei setze ich neben meinem Know-How modernste Software ein. Holen Sie sich ihr individuelles Angebot ein und leisten Sie auch ein Beitrag zur Energiewende, indem Sie von staatlichen Förderungen Gebrauch machen.</p>
      <p class="signature">M. Eng. Torben Wiskow<br>Energy consultant / planning engineer<br>Volmar Haus<br>Lindholzgasse 7C<br>47263 Gelsenkirchen<br>Tel: 0152 / 871 43 06<br>E-mail: info@Volmar-Haus.de</p>
    </div>
  </section>

  <section class="panel p3">
    <h2 class="heading">Leistungen</h2>
    <div class="services">
      <div class="service"><svg width="32" height="32" viewBox="0 0 32 32"><circle cx="16" cy="16" r="14" fill="none" stroke="#1c7cc4" stroke-width="1.5"/><path d="M17 8l-5 9h4l-1 7 5-9h-4z" fill="#15a9b3"/></svg>Energieberatung</div>
      <div class="service"><svg width="32" height="32" viewBox="0 0 32 32"><circle cx="16" cy="16" r="14" fill="none" stroke="#1c7cc4" stroke-width="1.5"/><circle cx="16" cy="14" r="5" fill="none" stroke="#15a9b3" stroke-width="1.5"/><path d="M9 22h14" stroke="#1c7cc4" stroke-width="1.5"/></svg>Fördermittelberatung<br>und -beantragung</div>
      <div class="service"><svg width="32" height="32" viewBox="0 0 32 32"><circle cx="16" cy="16" r="14" fill="none" stroke="#1c7cc4" stroke-width="1.5"/><circle cx="16" cy="13" r="3" fill="#15a9b3"/><path d="M10 22a6 5 0 0 1 12 0z" fill="#15a9b3"/></svg>Individueller<br>Sanierungsfahrplan (iSFP)</div>
      <div class="service"><svg width="32" height="32" viewBox="0 0 32 32"><circle cx="16" cy="16" r="14" fill="none" stroke="#1c7cc4" stroke-width="1.5"/><rect x="10" y="10" width="12" height="12" fill="none" stroke="#15a9b3" stroke-width="1.5"/></svg>PUL-Einzelmaßnahmen<br>wie z. B. Dämmung der<br>Gebäudehülle oder<br>Fenstertausch uvm.</div>
      <div class="service"><svg width="32" height="32" viewBox="0 0 32 32"><circle cx="16" cy="16" r="14" fill="none" stroke="#1c7cc4" stroke-width="1.5"/><rect x="10" y="9" width="12" height="14" rx="1" fill="none" stroke="#15a9b3" stroke-width="1.5"/><path d="M12 14h8M12 18h6" stroke="#1c7cc4"/></svg>Energieausweise</div>
      <div class="service"><svg width="32" height="32" viewBox="0 0 32 32"><circle cx="16" cy="16" r="14" fill="none" stroke="#1c7cc4" stroke-width="1.5"/><path d="M11 22c3-3-1-6 2-10M16 22c3-3-1-6 2-10M21 22c3-3-1-6 2-10" fill="none" stroke="#15a9b3" stroke-width="1.5"/></svg>Heizlastberechnung<br>nach DIN EN 12831</div>
      <div class="service"><svg width="32" height="32" viewBox="0 0 32 32"><circle cx="16" cy="16" r="14" fill="none" stroke="#1c7cc4" stroke-width="1.5"/><path d="M9 17l7-7 7 7M11 15v7h10v-7" fill="none" stroke="#15a9b3" stroke-width="1.5"/></svg>TbH-Effizienzhaus-Planung<br>(Neubau und Bestand)</div>
      <div class="service"><svg width="32" height="32" viewBox="0 0 32 32"><circle cx="16" cy="16" r="14" fill="none" stroke="#1c7cc4" stroke-width="1.5"/><path d="M10 22h12M16 9v13M12 13h8" stroke="#15a9b3" stroke-width="1.5"/></svg>Hydraulischer Abgleich<br>nach Verfahren A/B</div>
      <div class="service"><svg width="32" height="32" viewBox="0 0 32 32"><circle cx="16" cy="16" r="14" fill="none" stroke="#1c7cc4" stroke-width="1.5"/><path d="M16 8l7 4v8l-7 4-7-4v-8z" fill="none" stroke="#15a9b3" stroke-width="1.5"/></svg>Planung klimafreundlicher<br>Neubau (KFN)</div>
      <div class="service"><svg width="32" height="32" viewBox="0 0 32 32"><circle cx="16" cy="16" r="14" fill="none" stroke="#1c7cc4" stroke-width="1.5"/><path d="M12 19c2-2-1-5 1-8M16 19c2-2-1-5 1-8M20 19c2-2-1-5 1-8M10 22h12" fill="none" stroke="#15a9b3" stroke-width="1.5"/></svg>Heizflächenauslegung</div>
      <div class="service last"><svg width="32" height="32" viewBox="0 0 32 32"><circle cx="16" cy="16" r="14" fill="none" stroke="#1c7cc4" stroke-width="1.5"/><rect x="10" y="10" width="12" height="9" fill="none" stroke="#15a9b3" stroke-width="1.5"/><path d="M16 19v4M12 23h8" stroke="#1c7cc4" stroke-width="1.5"/></svg>Wärmepumpen<br>(Beratung und Auslegung)</div>
    </div>
  </section>
</div>

</body>
</html>
```